"Parker's True Grain Woodwork" with a logo of a saw blade and handplane combined

Need a business card logo with a saw blade and hand plane
combined with Parker's True Grain Woodwork on it, and a unique design.

Woodworking has been in my family for generations, from carpentry, to milling logs for old farm homes and barns in the 1930's and 1940's. My grandfather had a small carpentry business from his home,and passed his skills down to my father who also did woodworking from his own small business. Having the passion for woodwork in my blood, I'm trying to continue with my own small business doing custom fine woodwork such as tables, small cabinetry and even outdoor projects to suite the customers needs. All my projects start with a rough piece of lumber, what ever the species suited for the project, and is milled to dimensions , assembled, and finished all by hand for a true handcrafted project.

My target market would be people who want a custom handmade piece, something that they can't find in stores and is unique. Also people who are willing to pay and appreciate the value, which is sometimes a hard market to find.

As far as design, I think I would like to get a sleek looking saw blade on the card combined with a hand plane some how. Background colour maybe a dark wood texture or grey? Colours I like are grey, black, reds, white, yellows but depending on how the card is looking I'm not afraid to use a cool colour to make something stand out. Just want the card to flow ,look clean and unique. Lettering I like serif and script or something similar to these that looks good on the card.

Facebook page is under Parker's True Grain Woodwork
Updates

If I could get logo on the card, a saw blade, hand plane or combine both together would be nice! Added Saturday, June 11, 2016

Target Market(s)

People that like a unique hand made project built to last

Industry/Entity Type

Business

Contact Information for Business Card

Parkers True Grain Woodwork
Hand crafted by: Owen Parker
Phone: 905 618-2297
Address: 412 Birchview Rd. Niagara-On-The-Lake Ont.
Email: parkerstruegrain@mailbox-example.com
Facebook: Parkers True Grain Woodwork
prefer icons for the info!

Font styles to use
Serif
Script

Requirements
Must have
• Nice clean look, little bit bold with an elegant taste
• Prefer black lettering
Nice to have
• I like silver for the saw blade and silver with brown handles on the hand plane!
Should not have
• Bright colours

```html
<!DOCTYPE html>
<html lang="en">
<head>
<meta charset="UTF-8">
<title>Parker's True Grain Woodwork – Business Card</title>
<link rel="stylesheet" href="https://fonts.googleapis.com/css2?family=Roboto+Slab:wght@600;700&family=Open+Sans:wght@400;600&display=swap">
<style>
  :root {
    --stage: #d9d4cc;
    --brown-light: #a8752e;
    --brown-mid: #7a4f1b;
    --brown-dark: #3e2509;
    --black: #0c0c0c;
    --black-soft: #262626;
    --grey-light: #b9b9b9;
    --grey-mid: #7d7d7d;
    --grey-dark: #4b4b4b;
    --stripe: #8a5a22;
    --silver: #c9c9c9;
    --white: #ffffff;
    --tag-blue: #4a6aa8;
  }
  * { box-sizing: border-box; margin: 0; padding: 0; }
  html, body {
    width: 1200px; height: 843px; overflow: hidden;
    background: var(--stage);
  }
  .canvas { position: relative; width: 1200px; height: 843px; }

  .card {
    position: absolute;
    width: 560px; height: 320px;
    overflow: hidden;
    box-shadow: 0 10px 28px rgba(0,0,0,.35);
  }

  /* Back card */
  .card-back {
    left: 70px; top: 90px;
    background: radial-gradient(ellipse at 50% 20%, var(--brown-light) 0%, var(--brown-mid) 55%, var(--brown-dark) 100%);
  }
  .card-back .brand { position: absolute; left: 0; right: 0; top: 140px; }
  .card-back .brand-name { font-size: 24px; }
  .card-back .brand-dot { width: 32px; height: 32px; }

  /* Brand line */
  .brand {
    display: flex; align-items: center; justify-content: center; gap: 10px;
  }
  .brand-dot {
    width: 28px; height: 28px; border-radius: 50%;
    background: var(--silver);
    flex: none;
  }
  .brand-name {
    font-family: "Roboto Slab", serif;
    font-weight: 700;
    font-size: 20px;
    letter-spacing: .3px;
    color: var(--white);
    text-transform: uppercase;
    line-height: 1;
    white-space: nowrap;
  }

  /* Front card */
  .card-front {
    left: 570px; top: 430px;
    background: linear-gradient(160deg, var(--black-soft) 0%, var(--black) 45%, var(--black-soft) 100%);
  }
  .card-front .shape { position: absolute; inset: 0; }
  .card-front .brand { position: absolute; left: 0; right: 0; top: 100px; }

  .social-tile {
    position: absolute; right: 28px; top: 40px;
    width: 32px; height: 32px; border-radius: 5px;
    background: var(--tag-blue);
  }

  .contact {
    position: absolute; left: 30px; top: 205px;
    color: var(--white);
    font-family: "Open Sans", sans-serif;
  }
  .contact-name {
    font-family: "Roboto Slab", serif;
    font-weight: 600;
    font-size: 18px;
    line-height: 24px;
    letter-spacing: .3px;
    text-transform: uppercase;
    white-space: nowrap;
  }
  .contact-line {
    display: flex; align-items: center; gap: 8px;
    font-size: 14px;
    line-height: 18px;
    margin-top: 4px;
    white-space: nowrap;
  }
  .contact-line svg { width: 13px; height: 13px; flex: none; }
</style>
</head>
<body>
<main class="canvas">

  <section class="card card-back" aria-label="Business card back">
    <div class="brand">
      <span class="brand-dot"></span>
      <span class="brand-name">Parker's True Grain Woodwork</span>
    </div>
  </section>

  <section class="card card-front" aria-label="Business card front">
    <svg class="shape" viewBox="0 0 560 320" preserveAspectRatio="none" aria-hidden="true">
      <defs>
        <linearGradient id="panelGrey" x1="0" y1="0" x2="1" y2="1">
          <stop offset="0" stop-color="#b9b9b9"/>
          <stop offset=".5" stop-color="#7d7d7d"/>
          <stop offset="1" stop-color="#4b4b4b"/>
        </linearGradient>
      </defs>
      <polygon points="0,177 250,172 560,292 560,320 0,320" fill="url(#panelGrey)"/>
      <polyline points="0,175 250,170 560,290" fill="none" stroke="#8a5a22" stroke-width="6"/>
    </svg>

    <div class="brand">
      <span class="brand-dot"></span>
      <span class="brand-name">Parker's True Grain Woodwork</span>
    </div>

    <span class="social-tile" aria-label="Social page"></span>

    <div class="contact">
      <p class="contact-name">Owen Parker - CEO/Founder</p>
      <p class="contact-line">412 Birchview Rd, Niagara-On-The-Lake Ont.</p>
      <p class="contact-line">
        <svg viewBox="0 0 24 24" aria-hidden="true"><path fill="#fff" d="M6.6 10.8a15.1 15.1 0 0 0 6.6 6.6l2.2-2.2c.3-.3.7-.4 1-.2 1.1.4 2.3.6 3.6.6.6 0 1 .4 1 1V20c0 .6-.4 1-1 1A17 17 0 0 1 3 4c0-.6.4-1 1-1h3.5c.6 0 1 .4 1 1 0 1.3.2 2.5.6 3.6.1.3 0 .7-.2 1z"/></svg>
        905 618-2297
      </p>
      <p class="contact-line">
        <svg viewBox="0 0 24 24" aria-hidden="true"><rect x="2" y="5" width="20" height="14" rx="1" fill="#fff"/><path d="M2 6l10 7 10-7" fill="none" stroke="#777" stroke-width="1.6"/></svg>
        parkerstruegrain@mailbox-example.com
      </p>
    </div>
  </section>

</main>
</body>
</html>
```